Bramwell Dental personal information forms

We are a Dental Practice that require an update to our information forms, there are 3 versions of it.
I will attach our old ones, we need to keep the same information on there, we just want them to look better and use our current logo and colours.
Our website is www.bramwelldental-example.net
Our facebook is www.facebook.com/bramwelldentalkestonwalk/
..................................................................................................

Target Market(s)

Everyone, easy to read

Industry/Entity Type

Dental Clinic

Colors
0692cd
34a6d7
cee9f5
ffffff
0255a3
3276b5

Requirements
Must have
• Logo
• Our colours
• same information as the uploaded versions
Should not have
• any other colour besides the blues, black and white

```html
<!DOCTYPE html>
<html lang="en">
<head>
<meta charset="utf-8">
<title>Bramwell Dental – Medical History Form</title>
<link href="https://fonts.googleapis.com/css2?family=Montserrat:ital,wght@0,400;0,500;0,700;1,400&display=swap" rel="stylesheet">
<style>
  :root {
    --blue-deep: #0255a3;
    --blue-main: #0692cd;
    --blue-mid: #3276b5;
    --blue-soft: #34a6d7;
    --blue-pale: #cee9f5;
    --panel: #dcecf4;
    --paper: #eef4f6;
    --ink: #111820;
    --white: #ffffff;
    --backdrop: #b4dfe2;
  }
  * { box-sizing: border-box; margin: 0; padding: 0; }
  html, body { width: 1200px; height: 1200px; overflow: hidden; }
  body {
    background: var(--backdrop);
    font-family: "Montserrat", Arial, sans-serif;
    color: var(--ink);
    display: flex; align-items: center; justify-content: center;
  }
  .form-page {
    position: relative;
    width: 830px; height: 1160px;
    background: var(--paper);
    display: flex; flex-direction: column;
    box-shadow: 0 6px 24px rgba(2, 85, 163, 0.18);
  }
  .header-band {
    height: 150px;
    background: linear-gradient(100deg, var(--blue-deep) 0%, var(--blue-mid) 55%, var(--blue-main) 100%);
    display: flex; justify-content: flex-end; align-items: center;
    padding-right: 56px;
  }
  .brand-name {
    color: var(--white);
    font-weight: 500;
    font-size: 46px;
    letter-spacing: 1px;
  }
  .intro-row {
    display: flex; justify-content: space-between; align-items: flex-start;
    padding: 22px 48px 0 48px;
  }
  .practitioners { font-size: 15px; line-height: 1.3; padding-top: 34px; }
  .sticker-box {
    width: 300px; height: 62px;
    border: 1.5px solid var(--ink);
    display: flex; align-items: center; justify-content: center;
    font-style: italic; font-size: 15px;
  }
  .welcome { padding: 18px 48px 14px; font-size: 13.5px; line-height: 1.35; }
  .welcome strong { font-weight: 700; font-size: 14.5px; display: block; margin-bottom: 2px; }
  .history-panel {
    margin: 0 36px;
    background: linear-gradient(180deg, var(--panel), var(--blue-pale));
    padding: 14px 16px 16px;
    display: flex; flex-direction: column; gap: 9px;
    font-size: 13.5px;
  }
  .question-head { display: flex; justify-content: space-between; align-items: flex-end; gap: 16px; line-height: 1.3; }
  .answer-options { display: flex; gap: 14px; white-space: nowrap; font-size: 13px; }
  .answer-options span, .condition-list li { display: flex; align-items: center; gap: 5px; }
  .tick-box {
    display: inline-block; width: 12px; height: 12px;
    border: 1px solid var(--ink); background: var(--white); flex: none;
  }
  .answer-line { height: 26px; background: var(--white); border: 1px solid #8aa3b3; margin-top: 3px; }
  .condition-columns { display: flex; gap: 28px; margin-top: 4px; }
  .condition-list { list-style: none; line-height: 1.42; flex: 1; }
  .declaration { padding: 26px 60px 0; font-size: 15px; line-height: 1.4; }
  .signature-row { padding: 26px 60px 0; font-size: 15px; display: flex; gap: 10px; }
  .signature-row .fill { border-bottom: 1px dashed var(--ink); display: inline-block; }
  .footer-band { margin-top: auto; height: 20px; background: var(--blue-main); }
</style>
</head>
<body>
  <main class="form-page">
    <header class="header-band">
      <span class="brand-name">Bramwell Dental</span>
    </header>

    <section class="intro-row">
      <p class="practitioners">Dr. Peter Halloran &amp; Dr. Simon Ashdown<br>Dental Surgeons</p>
      <div class="sticker-box">Affix patient sticker here.</div>
    </section>

    <section class="welcome">
      <strong>Welcome back to our practice!</strong>
      THIS INFORMATION IS CONFIDENTIAL and is necessary to enable us to offer you THE BEST POSSIBLE CARE. It is now mandatory to have a written updated medical history every 2 years and we would appreciate your time in thoroughly completing this form.
    </section>

    <section class="history-panel">
      <div class="question">
        <div class="question-head">
          <p>Are you currently or have you taken any prescribed medication or dietary supplements in the last 12 months? (If YES, please list below)</p>
          <div class="answer-options"><span><i class="tick-box"></i>YES</span><span><i class="tick-box"></i>NO</span></div>
        </div>
        <div class="answer-line"></div>
      </div>

      <div class="question">
        <div class="question-head">
          <p>Allergies / Reactions? (If YES, please list below)</p>
          <div class="answer-options"><span><i class="tick-box"></i>YES</span><span><i class="tick-box"></i>NO</span></div>
        </div>
        <div class="answer-line"></div>
      </div>

      <div class="question">
        <p>Have you ever had or are you suffering from any of the following? Please tick any that apply:</p>
        <div class="condition-columns">
          <ul class="condition-list">
            <li><i class="tick-box"></i>Rheumatic fever</li>
            <li><i class="tick-box"></i>Epilepsy</li>
            <li><i class="tick-box"></i>Asthma</li>
            <li><i class="tick-box"></i>Tuberculosis</li>
            <li><i class="tick-box"></i>Radiation Therapy</li>
            <li><i class="tick-box"></i>Dizziness, fainting</li>
            <li><i class="tick-box"></i>Hepatitis A B or C</li>
            <li><i class="tick-box"></i>Recent eye surgery</li>
          </ul>
          <ul class="condition-list">
            <li><i class="tick-box"></i>Diabetes</li>
            <li><i class="tick-box"></i>Kidney Disease</li>
            <li><i class="tick-box"></i>Heart Attack</li>
            <li><i class="tick-box"></i>High Blood Pressure</li>
            <li><i class="tick-box"></i>Bleeding problems</li>
            <li><i class="tick-box"></i>Artificial joints</li>
            <li><i class="tick-box"></i>Respiratory problems</li>
          </ul>
          <ul class="condition-list">
            <li><i class="tick-box"></i>HIV Positive</li>
            <li><i class="tick-box"></i>High cholesterol</li>
            <li><i class="tick-box"></i>Cancer</li>
            <li><i class="tick-box"></i>Pace-maker</li>
            <li><i class="tick-box"></i>Osteoporosis</li>
            <li><i class="tick-box"></i>Heart rate problems</li>
            <li><i class="tick-box"></i>Heart murmur</li>
          </ul>
        </div>
      </div>

      <div class="question">
        <div class="question-head">
          <p>Do you have any disease, condition or problem not listed above?</p>
          <div class="answer-options"><span><i class="tick-box"></i>YES</span><span><i class="tick-box"></i>NO</span></div>
        </div>
        <div class="answer-line"></div>
      </div>

      <div class="question">
        <div class="question-head">
          <p>Have you had surgery or been to hospital in the last 5 years?</p>
          <div class="answer-options"><span><i class="tick-box"></i>YES</span><span><i class="tick-box"></i>NO</span></div>
        </div>
        <div class="answer-line"></div>
      </div>

      <div class="question">
        <div class="question-head">
          <p>For Women: Are you pregnant? If yes, how many months?</p>
          <div class="answer-options"><span><i class="tick-box"></i>YES</span><span><i class="tick-box"></i>NO</span></div>
        </div>
        <div class="answer-line"></div>
      </div>

      <div class="question">
        <div class="question-head">
          <p>Do you currently or have you ever smoked?</p>
          <div class="answer-options"><span><i class="tick-box"></i>YES</span><span><i class="tick-box"></i>NO</span></div>
        </div>
        <div class="answer-line"></div>
      </div>
    </section>

    <section class="declaration">
      The information that I have provided is to the best of my knowledge true and correct and I understand that it is my responsibility to inform of any changes in my medical status.
    </section>

    <section class="signature-row">
      <span>Patient/Parent/Person Responsible Signature:</span>
      <span class="fill" style="width:150px"></span>
      <span>Date:</span>
      <span class="fill" style="width:110px"></span>
    </section>

    <footer class="footer-band"></footer>
  </main>
</body>
</html>
```